Bulldog themed background for Real Estate Purchase Letter

I need a phantom background or watermark on a standard 8 1/2" x 11" paper. I am going to put a letter over the background. I want a bulldog theme that is cute, funny and original. This letter is for a real estate project and we want to capture the person sub-consciously . Attached is my personal dogs. If you want to use them you can but not required. I have attached the letter that I am trying to emulate. I want bulldogs not horses.

Target Market(s)

45 years old and higher

Industry/Entity Type

Real Estate

Font styles to use
Serif
Sans Serif

Colors

Designer to choose colors to be used in the design.

Requirements
Must have
• fun, happiness, reassuring,
Should not have
• violence, negativity, unhappy

```html
<!DOCTYPE html>
<html lang="en">
<head>
<meta charset="utf-8">
<title>Keystone Realty – Purchase Letter</title>
<link href="https://fonts.googleapis.com/css2?family=Montserrat:wght@400;500;700&display=swap" rel="stylesheet">
<style>
  :root {
    --backdrop: #b4b4b4;
    --paper: #ffffff;
    --ink: #3a3a3a;
    --ink-strong: #231f20;
    --brand-blue: #2e6a96;
    --brand-navy: #1f5f8a;
    --wash-light: #fbf3df;
    --wash-mid: #efe3cf;
    --rule-dark: #b7782e;
    --rule-light: #f6dc8e;
  }
  * { margin: 0; padding: 0; box-sizing: border-box; }
  html, body {
    width: 1200px; height: 1200px; overflow: hidden;
    background: var(--backdrop);
  }
  body { font-family: "Montserrat", Arial, sans-serif; color: var(--ink); }
  .letter {
    position: absolute; left: 175px; top: 50px;
    width: 850px; height: 1100px;
    background: var(--paper);
  }
  .letter > * { position: absolute; }
  .watermark-area {
    left: 72px; top: 267px; width: 703px; height: 704px;
    border-radius: 60px;
    background: radial-gradient(circle at 50% 40%, var(--wash-light) 0%, var(--wash-mid) 75%);
    opacity: 0.75;
  }
  .recipient {
    left: 73px; top: 74px;
    font-size: 13.5px; line-height: 20px; letter-spacing: 0.2px;
  }
  .recipient-name { color: var(--brand-blue); }
  .agent-title {
    right: 75px; top: 114px;
    font-size: 13.5px; letter-spacing: 0.3px;
  }
  .letter-body {
    left: 73px; top: 350px; width: 710px;
    font-size: 12.6px; line-height: 27.2px; letter-spacing: 0.15px;
  }
  .letter-body p + p { margin-top: 27.2px; }
  .closing { left: 73px; top: 805px; font-size: 13px; }
  .signature { left: 73px; top: 870px; }
  .signature-name {
    font-weight: 700; font-size: 17px; color: var(--ink-strong); letter-spacing: 0.2px;
  }
  .signature-phone { font-size: 13px; margin-top: 2px; }
  .brand-mark {
    left: 560px; top: 840px; width: 215px;
    display: flex; align-items: center; gap: 10px; justify-content: flex-end;
    color: var(--brand-navy); font-weight: 700; font-size: 18px;
  }
  .brand-square { width: 22px; height: 22px; background: var(--brand-navy); border-radius: 4px; }
  .postscript {
    left: 73px; top: 972px; width: 710px;
    font-size: 16.5px; line-height: 24px; letter-spacing: 0.2px;
  }
  .footer-rule {
    left: 73px; top: 1042px; width: 702px; height: 2px;
    background: linear-gradient(90deg, var(--rule-dark), var(--rule-light) 35%, var(--rule-dark) 55%, var(--rule-light) 80%, var(--rule-dark));
  }
</style>
</head>
<body>
  <main class="letter">
    <div class="watermark-area" role="img" aria-label="Faint beige bulldog watermark behind the letter"></div>

    <address class="recipient" style="font-style:normal">
      <div><span class="recipient-name">MR. OUTTA STATEOWNER</span> - &nbsp;Non PA Address</div>
      <div>4820 Harbor Lane</div>
      <div>LAKEVIEW FL 32000-1100</div>
    </address>
    <div class="agent-title">LICENSED REAL STATE AGENT</div>

    <section class="letter-body">
      <p>This is a sample letter that has been placed to demonstrate typing remat (Your Company). letterhead design. When positioned properly, it will serve to work in harmony with all other elements letterhead. This letterhead design is meant to project an image</p>
      <p>This letterhead design is meant project an image of professionalism reliability. By using simple aligen we have created a very spacious feeling. The simplicity suggest &nbsp;rengththe spaciousnes contributes haesthetics the layout. These basic qualities along with the (Your Company)</p>
      <p>look and helps reinforce the (Your Company) brand. letterhead design is meant to project an image design. When positioned properly, it will serve to work in harmony all the other elements letterhead. sionalism and reliability.</p>
      <p>This letterhead design is based on the (Form of your logo) form (Your Company) logo. Each stationery we have created a very spacious feeling. The simplicity suggests strength the spaciousnes contribute part of the (Form of your logo).</p>
    </section>

    <div class="closing">Sincearly,</div>
    <div class="signature">
      <div class="signature-name">Dana Whitfield</div>
      <div class="signature-phone">(xxx) XXXX-XXXXX</div>
    </div>

    <div class="brand-mark"><span class="brand-square"></span><span>Keystone Realty</span></div>

    <p class="postscript">P.S. &nbsp;If you would like to e- mail me information and pictures of your property, Please Send them to dana@keystonemail.com</p>
    <div class="footer-rule"></div>
  </main>
</body>
</html>
```